New Business Card for Auto Repair and Performance Shop!

Need a redesign on a card that we have used for a while now. Something more update and modern, Serious but not too serious. Something confident, that shows the client that we are bespoke. Adding value.

Target Market(s)

Foreign Auto Repair and Performance

Industry/Entity Type

Automotive

Contact Information for Business Card

Utilize Logo, would like to change car silhouette to something Veltra,

Font styles to use
Sans Serif

Requirements
Must have
• business name, address, website, phone number.
MotoSerenix
4918 W. Birchwell Rd
Fernmont, Q.L. 00000
1-555-487-3106
www.moto-serenix-example.com

Specializing in Asian, European, and Domestic Auto Repair, Performance and Fabrication.

Clear space on back to for space to write appointment time and which client advisor helped the client.
Nice to have
• Up to the designers,

```html
<!DOCTYPE html>
<html lang="en">
<head>
<meta charset="utf-8">
<title>MotoSerenix Business Card</title>
<link rel="stylesheet" href="https://fonts.googleapis.com/css2?family=Lato:wght@300;400;700&display=swap">
<style>
  :root {
    --page: #e6e4e1;
    --card: #262626;
    --card-edge: #1c1c1c;
    --ink: #ffffff;
    --ink-soft: #c9c9c9;
    --ink-muted: #8d8d8d;
    --emboss: #333333;
    --accent: #b22a2a;
  }
  * { box-sizing: border-box; margin: 0; padding: 0; }
  html, body { width: 1200px; height: 900px; overflow: hidden; }
  body {
    background: var(--page);
    font-family: "Lato", sans-serif;
    display: flex;
    align-items: center;
    justify-content: center;
    gap: 60px;
  }
  .card {
    position: relative;
    width: 525px;
    height: 300px;
    background: var(--card);
    border-radius: 26px;
    box-shadow: 0 2px 0 var(--card-edge), 0 14px 30px rgba(0,0,0,.25);
    overflow: hidden;
    color: var(--ink);
  }

  /* front */
  .corner-tab {
    position: absolute;
    width: 64px;
    height: 18px;
    background: var(--ink);
  }
  .corner-tab--top { left: 0; top: 0; border-bottom-right-radius: 18px; }
  .corner-tab--bottom { left: 0; bottom: 0; border-top-right-radius: 18px; }
  .brand-emboss {
    position: absolute;
    right: 28px;
    top: 34px;
    font-weight: 700;
    font-size: 54px;
    letter-spacing: 1px;
    color: var(--emboss);
  }
  .person {
    position: absolute;
    left: 36px;
    top: 128px;
  }
  .person__name { font-size: 22px; font-weight: 400; }
  .person__name strong { font-weight: 700; }
  .person__role {
    font-size: 13px;
    font-weight: 300;
    color: var(--ink-muted);
    text-align: right;
    margin-top: 2px;
  }
  .contact-list {
    position: absolute;
    left: 200px;
    right: 20px;
    top: 126px;
    list-style: none;
  }
  .contact-list li {
    display: flex;
    align-items: center;
    gap: 14px;
    font-size: 14px;
    font-weight: 400;
    height: 32px;
    white-space: nowrap;
  }
  .contact-list svg { width: 16px; height: 16px; flex: none; fill: var(--ink); }

  /* back */
  .back-brand {
    position: absolute;
    right: 34px;
    top: 28px;
    display: flex;
    align-items: center;
    gap: 8px;
    font-size: 22px;
    font-weight: 700;
  }
  .back-brand__dot {
    width: 10px; height: 10px; border-radius: 50%;
    background: var(--accent);
  }
  .tagline {
    position: absolute;
    left: 34px;
    right: 34px;
    top: 78px;
    font-size: 14px;
    font-weight: 400;
    line-height: 1.3;
    text-transform: uppercase;
    color: var(--ink-soft);
    text-align: right;
  }
  .note-fields {
    position: absolute;
    left: 34px;
    right: 34px;
    top: 160px;
  }
  .note-field {
    display: flex;
    align-items: center;
    margin-bottom: 16px;
    font-size: 14px;
    color: var(--ink-soft);
  }
  .note-field__label { width: 140px; }
  .note-field__colon { width: 16px; }
  .note-field__line {
    flex: 1;
    height: 30px;
    background: var(--ink);
    border-radius: 8px;
  }
</style>
</head>
<body>

  <section class="card card--front" aria-label="Card front">
    <span class="corner-tab corner-tab--top"></span>
    <span class="corner-tab corner-tab--bottom"></span>
    <div class="brand-emboss">MotoSerenix</div>

    <div class="person">
      <p class="person__name"><strong>Lorem</strong> ipsum</p>
      <p class="person__role">founder</p>
    </div>

    <ul class="contact-list">
      <li>
        <svg viewBox="0 0 16 16" aria-hidden="true"><path d="M3 1h3l1.5 4-2 1.3a9 9 0 0 0 4.2 4.2L11 8.5l4 1.5v3a2 2 0 0 1-2 2A12 12 0 0 1 1 3a2 2 0 0 1 2-2z"/></svg>
        <span>1-555-487-3106</span>
      </li>
      <li>
        <svg viewBox="0 0 16 16" aria-hidden="true"><path d="M8 1l6 14-6-3.5L2 15z"/></svg>
        <span>info@moto-serenix-example.com</span>
      </li>
      <li>
        <svg viewBox="0 0 16 16" aria-hidden="true"><path d="M8 1a7 7 0 1 0 0 14A7 7 0 0 0 8 1zm0 1.3c.9 0 1.9 1.6 2.2 4.2H5.8C6.1 3.9 7.1 2.3 8 2.3zM2.4 6.5h2.2a13 13 0 0 0 0 3H2.4a5.7 5.7 0 0 1 0-3zm3.4 4.2h4.4C9.9 13.1 8.9 13.7 8 13.7s-1.9-.6-2.2-3zm5.6-1.2a13 13 0 0 0 0-3h2.2a5.7 5.7 0 0 1 0 3zM5.8 7.7h4.4a12 12 0 0 1 0 .6v.6H5.8v-1.2z"/></svg>
        <span>www.moto-serenix-example.com</span>
      </li>
      <li>
        <svg viewBox="0 0 16 16" aria-hidden="true"><path d="M8 1l7 6.5h-2V15H9.5v-4h-3v4H3V7.5H1z"/></svg>
        <span>4918 W. Birchwell Rd Fernmont, Q.L. 00000</span>
      </li>
    </ul>
  </section>

  <section class="card card--back" aria-label="Card back">
    <div class="back-brand"><span class="back-brand__dot"></span>MotoSerenix</div>
    <p class="tagline">Specializing in Asian, European, and Domestic Auto Repair,<br>Performance and Fabrication.</p>

    <div class="note-fields">
      <div class="note-field">
        <span class="note-field__label">Appointment time</span>
        <span class="note-field__colon">:</span>
        <span class="note-field__line"></span>
      </div>
      <div class="note-field">
        <span class="note-field__label">Client-advisor</span>
        <span class="note-field__colon">:</span>
        <span class="note-field__line"></span>
      </div>
    </div>
  </section>

</body>
</html>
```